Trade show banner and popup for Plexa Works

Use the existing logo and graphic elements and text of sales arguments from our web site www.plexaworks-demo.com to create a backdrop banner and popup banner.

Both banners are trim size 181.7 x 76.2 cm. One is vertical, the other is horizontal. The full bleed size is 767 x 1824 mm 2265 x 5385 pixels.

We have a 2m by 2m corner stand on a tradeshow. The banner will be on one wall, the vertical against the other wall by the aisle.

Target Market(s)

This display is for a manufacturing trade show. The typical visitors are middle age engineers.

Industry/Entity Type

Trade

Requirements
Must have
• Our logo.
Nice to have
• One of the main benefits of our system is that it can be created for no charge with an online signup which is available at the show. We want to tempt people off the aisles to do this. So the vertical banner could have the words "Create your own online ERP system here for no charge"
Should not have
• Small text, these banners should attract attention of passers by in a trade show.

```html
<!DOCTYPE html>
<html lang="en">
<head>
<meta charset="utf-8">
<title>Plexa Works – Trade Show Banners</title>
<link href="https://fonts.googleapis.com/css2?family=Open+Sans:ital,wght@0,400;0,600;1,400;1,700&display=swap" rel="stylesheet">
<style>
  :root {
    --stage: #000000;
    --paper: #ffffff;
    --ink: #222222;
    --gold: #c9c28e;
    --gold-dark: #a39c66;
    --brand-blue: #1a78bf;
    --sky-top: #3f9fe6;
    --sky-mid: #9fd0f2;
    --sea: #3f8fa6;
    --grass: #8a9a45;
  }
  * { box-sizing: border-box; margin: 0; padding: 0; }
  html, body {
    width: 1200px;
    height: 900px;
    overflow: hidden;
    background: var(--stage);
    font-family: "Open Sans", Arial, sans-serif;
  }
  .canvas { position: relative; width: 1200px; height: 900px; }

  .banner { position: absolute; background: var(--paper); }
  .banner--wide { left: 83px; top: 106px; width: 678px; height: 285px; }
  .banner--tall { left: 814px; top: 97px; width: 284px; height: 680px; }

  .brand {
    position: absolute;
    display: flex;
    align-items: center;
    gap: 9px;
  }
  .brand__dot {
    width: 40px; height: 40px;
    border-radius: 50%;
    background: var(--gold);
    flex: none;
  }
  .brand__name {
    font-weight: 600;
    font-size: 22px;
    line-height: 1;
    color: var(--ink);
    letter-spacing: 0.5px;
  }
  .banner--wide .brand { left: 25px; top: 19px; }
  .banner--tall .brand { left: 50px; top: 20px; }

  .scene {
    position: absolute;
    left: 0; width: 100%;
    background: linear-gradient(180deg,
      var(--sky-top) 0%,
      var(--sky-mid) 52%,
      #d8ecf5 62%,
      var(--sea) 70%,
      #6fa7a8 76%,
      var(--grass) 84%,
      #7d8c3a 100%);
  }
  .banner--wide .scene { top: 69px; height: 177px; }
  .banner--tall .scene { top: 79px; height: 152px; }

  .tagline {
    position: absolute;
    right: 28px; top: 55px;
    color: var(--paper);
    font-style: italic;
    font-size: 19px;
    letter-spacing: 3.6px;
  }

  .url-band {
    position: absolute;
    left: 0; width: 100%;
    background: var(--gold);
    color: var(--ink);
    font-style: italic;
    font-size: 14px;
    letter-spacing: 2.8px;
    display: flex;
    align-items: center;
  }
  .banner--wide .url-band { top: 262px; height: 23px; justify-content: flex-end; padding-right: 14px; }
  .banner--tall .url-band { top: 647px; height: 33px; justify-content: center; font-size: 13px; letter-spacing: 2.2px; }

  .accent-bar {
    position: absolute;
    left: 0; top: 238px;
    width: 131px; height: 13px;
    background: linear-gradient(90deg, #2a8ad0, var(--brand-blue));
  }

  .offer {
    position: absolute;
    left: 0; width: 100%;
    top: 400px;
    text-align: center;
    font-style: italic;
    font-weight: 700;
    color: var(--ink);
    font-size: 27px;
    line-height: 46px;
    letter-spacing: -0.4px;
  }
  .offer__highlight {
    display: block;
    margin-top: 14px;
    color: var(--brand-blue);
    font-size: 38px;
    line-height: 46px;
  }
</style>
</head>
<body>
<main class="canvas">

  <section class="banner banner--wide" aria-label="Horizontal backdrop banner">
    <div class="brand">
      <span class="brand__dot"></span>
      <span class="brand__name">Plexa Works</span>
    </div>
    <div class="scene" role="img" aria-label="Photo of a person raising arms beside a desk with a laptop on a grassy dune by the sea under a blue sky">
      <p class="tagline">easy efficient everwhere</p>
    </div>
    <div class="url-band">www.plexaworks-demo.com</div>
  </section>

  <section class="banner banner--tall" aria-label="Vertical popup banner">
    <div class="brand">
      <span class="brand__dot"></span>
      <span class="brand__name">Plexa Works</span>
    </div>
    <div class="scene" role="img" aria-label="Photo of a person raising arms beside a desk with a laptop on a grassy dune by the sea under a blue sky"></div>
    <div class="accent-bar"></div>
    <p class="offer">
      Create your own<br>
      online ERP system<br>
      here for
      <span class="offer__highlight">No Charge</span>
    </p>
    <div class="url-band">www.plexaworks-demo.com</div>
  </section>

</main>
</body>
</html>
```